Permanent Makeup (cosmetics salon) Brochure

We need a 2-4 sites brochure for our Permanent Makeup (cosmetics salon). Our company is based in Austria / Vienna. -> Our homepage is www.mk-hollmeister.at
This brochure should show which treatments we provide ot our customers.

I've uploaded our old brochure, the content (text) would be nearly the same (look form "Must Haves", pics have to be new (look uploaded pics)
The old brochure is to dark. -> look for our homepage maybe you can make it like this

Target Market(s)

woman, age 25-70 years who wants to have permanent makeup on eyebrows, lips or eyeliner

Industry/Entity Type

Beauty Salon

Requirements
Must have
• pics which are uploaded.

*This text (somithing about our business)
"Für Frau Hollmeister ist Permanent Makeup ein Kunsthandwerk. Das Team von MK-Hollmeister ist spezialisiert auf natürliches Permanent Makeup damit der individuelle Typ jeder Kundin am schönsten zum Ausdruck kommt."

*We do this treatments: (english)
+ Augenbrauen Microblading (eyebrows)
+ Augenbrauen Permanent Makeup (eyebrows2)
+ Lidstrich Permanent Makeup (eyeliner)
+ Lip Blushing (lips)
+ Lippen Permanent Makeup (lips2)

* Our addresses (2 locations)
Wien
Lerchengasse 7b/21, 1080 Wien
Tel: 01/5826107

Villach
Birkenstraße 24, 9581 St. Ulrich
Tel: 0664/3158902

Mail: info@mk-hollmeister.at
www.mk-hollmeister.at

```html
<!DOCTYPE html>
<html lang="de">
<head>
<meta charset="utf-8">
<title>Marika Hollmeister Kosmetikstudio – Broschüre</title>
<link rel="stylesheet" href="https://fonts.googleapis.com/css2?family=Cinzel:wght@400;500&family=Signika:wght@300;400;600&display=swap">
<style>
:root{
  --bg:#dcdcdc;
  --paper:#ffffff;
  --ink:#1f1f1f;
  --gold:#d8b04a;
  --gold-light:#f3dc84;
  --gray-panel:#eceef0;
  --faint:#f1f2f4;
}
*{margin:0;padding:0;box-sizing:border-box}
html,body{width:1200px;height:1200px;overflow:hidden}
body{background:radial-gradient(circle at 50% 45%,#ececec,var(--bg));font-family:"Signika",sans-serif;font-weight:300;color:var(--ink);position:relative}
.spread{position:absolute;background:var(--paper);overflow:hidden;box-shadow:0 3px 8px rgba(0,0,0,.18)}
.spread--outer{left:107px;top:71px;width:986px;height:497px}
.spread--inner{left:106px;top:624px;width:991px;height:501px}
.spine{position:absolute;top:0;bottom:0;width:60px;background:linear-gradient(90deg,rgba(0,0,0,.08),rgba(0,0,0,0))}
.spread--outer .spine{left:497px}
.spread--inner .spine{left:494px;background:linear-gradient(90deg,rgba(0,0,0,.06),rgba(0,0,0,0))}
.spread--inner .spine-l{position:absolute;top:0;bottom:0;left:434px;width:60px;background:linear-gradient(270deg,rgba(0,0,0,.05),rgba(0,0,0,0))}
.deco{position:absolute;left:0;top:0;pointer-events:none}
.abs{position:absolute}
.photo{position:absolute}
.panel{position:absolute;background:var(--gray-panel)}
.center{transform:translateX(-50%);text-align:center;white-space:nowrap}

.brand{position:absolute;transform:translateX(-50%);text-align:center;white-space:nowrap}
.brand__name{font-family:"Signika",sans-serif;font-weight:300;font-size:25px;letter-spacing:2px;color:var(--ink);line-height:1}
.brand__tag{font-family:"Signika",sans-serif;font-weight:400;font-size:8.5px;letter-spacing:5px;margin-top:12px;color:var(--ink);padding-left:5px}

.reg{font-size:12.5px;font-weight:400}
.location{position:absolute;transform:translateX(-50%);text-align:center;white-space:nowrap;font-size:12.5px;line-height:19px;font-weight:300}
.location__city{font-weight:600;font-size:13px}
.divider{position:absolute;left:248px;top:255px;width:1px;height:61px;background:var(--gold)}
.icon{width:11px;height:11px;vertical-align:-1px;margin-right:3px}
.contact{font-size:12.5px;line-height:21px;font-weight:300}

.headline{position:absolute;font-family:"Cinzel",serif;color:var(--ink);white-space:nowrap;line-height:1}
.headline--gold{color:var(--gold);font-size:34px}
.headline--sub{font-size:17px;color:#333}
.headline--big{font-size:31px;color:#2a2a2a}
.hygiene{position:absolute;left:517px;top:436px;font-family:"Cinzel",serif;font-size:8px;line-height:14px;color:#666}

.tagline{position:absolute;font-family:"Cinzel",serif;font-weight:500;color:var(--gold);font-size:16px;white-space:nowrap}
.about{position:absolute;left:249px;top:343px;width:410px;transform:translateX(-50%);text-align:center;font-size:14.5px;line-height:25.5px;font-weight:300;color:#222}

.treatments-title{position:absolute;font-family:"Cinzel",serif;font-size:22px;color:#222;white-space:nowrap;font-weight:400}
.treatment{position:absolute;left:545px;width:403px;height:50px;background:linear-gradient(90deg,rgba(236,238,240,0),var(--faint) 40%,var(--faint));font-size:14px;font-weight:300;color:#222}
.treatment--right{background:linear-gradient(270deg,rgba(236,238,240,0),var(--faint) 40%,var(--faint))}
.treatment__img{position:absolute;top:0;width:146px;height:50px}
.treatment__img--l{left:0;border-right:2.5px solid var(--gold)}
.treatment__img--r{right:0;border-left:2.5px solid var(--gold)}
.treatment__label{position:absolute;top:15px;white-space:nowrap}
.treatment__label--l{left:164px}
.treatment__label--r{right:171px}
.services{position:absolute;left:740px;top:404px;transform:translateX(-50%);text-align:center;font-size:10px;line-height:17.3px;font-weight:300;white-space:nowrap;color:#222}
.services .sep{color:var(--gold);margin:0 3px}
</style>
</head>
<body>

<section class="spread spread--outer">
  <svg class="deco" width="986" height="497" viewBox="0 0 986 497">
    <defs>
      <linearGradient id="goldA" x1="0" y1="0" x2="1" y2="1">
        <stop offset="0" stop-color="#f5de86"/><stop offset=".5" stop-color="#d6ab3e"/><stop offset="1" stop-color="#f2d77a"/>
      </linearGradient>
      <filter id="soft" x="-50%" y="-50%" width="200%" height="200%"><feDropShadow dx="0" dy="4" stdDeviation="6" flood-opacity=".18"/></filter>
    </defs>
    <circle cx="118" cy="53" r="87" fill="none" stroke="url(#goldA)" stroke-width="12"/>
    <circle cx="600" cy="440" r="150" fill="none" stroke="#f0f1f3" stroke-width="28"/>
    <circle cx="755" cy="431" r="78" fill="none" stroke="url(#goldA)" stroke-width="12"/>
  </svg>
  <div class="spine"></div>

  <div class="panel" style="left:117px;top:47px;width:285px;height:158px"></div>
  <div class="photo" role="img" aria-label="Foto: Kosmetikerin im hellen Behandlungsraum neben der Behandlungsliege" style="left:95px;top:26px;width:285px;height:157px;background:linear-gradient(100deg,#c9c2c2,#dcd6d5 45%,#bdb6b6 70%,#e9e7e6)"></div>

  <div class="abs center reg" style="left:248px;top:220px">MK-Kosmetik 201800022222</div>

  <div class="location" style="left:134px;top:256px">
    <div class="location__city">Wien</div>
    <div>Lerchengasse 7b/21, 1080 Wien</div>
    <div><svg class="icon" viewBox="0 0 24 24"><path fill="#d8b04a" d="M6.6 10.8a15.1 15.1 0 0 0 6.6 6.6l2.2-2.2c.3-.3.7-.4 1-.2 1.1.4 2.3.6 3.6.6.6 0 1 .4 1 1V20c0 .6-.4 1-1 1A17 17 0 0 1 3 4c0-.6.4-1 1-1h3.5c.6 0 1 .4 1 1 0 1.3.2 2.5.6 3.6.1.3 0 .7-.2 1z"/></svg>01/5826107</div>
  </div>
  <div class="divider"></div>
  <div class="location" style="left:369px;top:256px">
    <div class="location__city">Villach</div>
    <div>Birkenstraße 24, 9581 St. Ulrich</div>
    <div><svg class="icon" viewBox="0 0 24 24"><path fill="#d8b04a" d="M6.6 10.8a15.1 15.1 0 0 0 6.6 6.6l2.2-2.2c.3-.3.7-.4 1-.2 1.1.4 2.3.6 3.6.6.6 0 1 .4 1 1V20c0 .6-.4 1-1 1A17 17 0 0 1 3 4c0-.6.4-1 1-1h3.5c.6 0 1 .4 1 1 0 1.3.2 2.5.6 3.6.1.3 0 .7-.2 1z"/></svg>0664/3158902</div>
  </div>

  <div class="abs center contact" style="left:250px;top:333px">
    <div><svg class="icon" viewBox="0 0 24 24"><path fill="#d8b04a" d="M2 5h20v14H2z"/><path d="M2 5l10 8 10-8" fill="none" stroke="#fff" stroke-width="2"/></svg>info@mk-hollmeister.at</div>
    <div><svg class="icon" viewBox="0 0 24 24" fill="none" stroke="#d8b04a" stroke-width="2"><circle cx="12" cy="12" r="10"/><path d="M2 12h20M12 2c3 3 3 17 0 20M12 2c-3 3-3 17 0 20"/></svg>www.mk-hollmeister.at</div>
  </div>

  <div class="brand" style="left:248px;top:410px">
    <div class="brand__name">Marika Hollmeister</div>
    <div class="brand__tag">KOSMETIKSTUDIO</div>
  </div>

  <div class="brand" style="left:736px;top:56px">
    <div class="brand__name">Marika Hollmeister</div>
    <div class="brand__tag">KOSMETIKSTUDIO</div>
  </div>

  <div class="headline headline--gold" style="left:520px;top:212px">Schönheit</div>
  <div class="headline headline--sub" style="left:520px;top:250px">KOMMT NICHT NUR</div>
  <div class="headline headline--big" style="left:520px;top:274px">VON</div>
  <div class="headline headline--big" style="left:553px;top:306px">INNEN</div>

  <div class="panel" style="left:720px;top:179px;width:227px;height:282px;background:#ebedef"></div>
  <div class="photo" role="img" aria-label="Foto: Porträt einer jungen Frau mit natürlichem Make-up" style="left:736px;top:163px;width:226px;height:281px;background:linear-gradient(120deg,#7b8791,#c89a81 35%,#e0b79d 60%,#9aa3aa)"></div>

  <svg class="deco" width="986" height="497" viewBox="0 0 986 497">
    <circle cx="506" cy="339" r="33" fill="none" stroke="url(#goldA)" stroke-width="7" filter="url(#soft)"/>
  </svg>

  <div class="hygiene">HYGIENEZERTIFIKAT<br>BGBl. II 262/2008</div>
</section>

<section class="spread spread--inner">
  <svg class="deco" width="991" height="501" viewBox="0 0 991 501">
    <defs>
      <linearGradient id="goldB" x1="0" y1="0" x2="1" y2="1">
        <stop offset="0" stop-color="#f5de86"/><stop offset=".5" stop-color="#d6ab3e"/><stop offset="1" stop-color="#f2d77a"/>
      </linearGradient>
    </defs>
    <circle cx="245" cy="65" r="168" fill="none" stroke="#f2f3f5" stroke-width="30"/>
    <circle cx="37" cy="475" r="38" fill="none" stroke="url(#goldB)" stroke-width="8"/>
    <circle cx="520" cy="16" r="68" fill="none" stroke="url(#goldB)" stroke-width="12"/>
  </svg>
  <div class="spine-l"></div>
  <div class="spine"></div>

  <div class="brand" style="left:249px;top:56px">
    <div class="brand__name">Marika Hollmeister</div>
    <div class="brand__tag">KOSMETIKSTUDIO</div>
  </div>

  <div class="panel" style="left:41px;top:181px;width:435px;height:125px"></div>
  <div class="photo" role="img" aria-label="Foto: Nahaufnahme eines Auges mit Wimpern und Augenbraue" style="left:17px;top:160px;width:444px;height:110px;background:linear-gradient(90deg,#5a3a2c,#b98470 30%,#c99a86 55%,#3b261e 85%,#111)"></div>
  <div class="tagline" style="left:57px;top:283px">Macht jeden Augenblick zu einer Augenweide</div>

  <p class="about">Für Frau Hollmeister ist Permanent Makeup ein Kunsthandwerk. Das Team von MK-Hollmeister ist spezialisiert auf natürliches Permanent Makeup damit der individuelle Typ jeder Kundin am schönsten zum Ausdruck kommt.</p>

  <h2 class="treatments-title" style="left:608px;top:40px">We Do This Treatments:</h2>

  <div class="treatment" style="top:84px">
    <div class="treatment__img treatment__img--l" role="img" aria-label="Foto: Augenbraue nach Microblading" style="background:linear-gradient(90deg,#d9c3a0,#a4806a 50%,#c79d88)"></div>
    <span class="treatment__label treatment__label--l">Augenbrauen Microblading</span>
  </div>
  <div class="treatment treatment--right" style="top:146px">
    <span class="treatment__label treatment__label--r">Augenbrauen Permanent Makeup</span>
    <div class="treatment__img treatment__img--r" role="img" aria-label="Foto: Augenbrauen mit Permanent Makeup" style="background:linear-gradient(90deg,#b88a74,#d9b39f 50%,#c69a85)"></div>
  </div>
  <div class="treatment" style="top:208px">
    <div class="treatment__img treatment__img--l" role="img" aria-label="Foto: Augen mit Lidstrich" style="background:linear-gradient(90deg,#a07a66,#e2c9bb 50%,#b58c78)"></div>
    <span class="treatment__label treatment__label--l">Lidstrich Permanent Makeup</span>
  </div>
  <div class="treatment treatment--right" style="top:270px">
    <span class="treatment__label treatment__label--r">Lip Blushing</span>
    <div class="treatment__img treatment__img--r" role="img" aria-label="Foto: Lippen nach Lip Blushing" style="background:linear-gradient(90deg,#e8c4b6,#d98478 50%,#e6bfb0)"></div>
  </div>
  <div class="treatment" style="top:332px">
    <div class="treatment__img treatment__img--l" role="img" aria-label="Foto: Lippen mit Permanent Makeup" style="background:linear-gradient(90deg,#d7a596,#cf7a6d 50%,#d9ab9c)"></div>
    <span class="treatment__label treatment__label--l">Lippen Permanent Makeup</span>
  </div>

  <div class="services">
    <div>Microblading auf höchstem Niveau<span class="sep">|</span>Permanent Make Up für Lippen</div>
    <div>Permanent Make Up als Lidstrich<span class="sep">|</span>Wimpernverlängerung<span class="sep">|</span>Gesichtsbehandlungen</div>
    <div>professionelles Make Up für Hochzeiten und alle Anlässe</div>
    <div>Sugaring / Haarentfernung<span class="sep">|</span>… und vieles mehr</div>
  </div>
</section>

</body>
</html>
```